Plumbing Truck design, emergency plumbing vehicle

Simple, highly effective plumbing design for plumbing vehicles

Brightwater Plumbing & Gas Services
(The Reliable Plumbing Specialists) moto

yellow, black and white colours (white as the vehicles are already painted white)

Clean and simple design

Attention grabbing

24hr Emergency service (listed on on the vehicle) possibly in red colour

Target Market(s)

plumbing

Industry/Entity Type

Plumbing

Colors
fbed22

Requirements
Must have
• Brightwater Plumbing & Gas Services
• (The Reliable Plumbing Specialists) moto
• yellow, black and white colours (white as the vehicles are already painted white)
• Clean and simple design
• Attention grabbing
• 24hr Emergency service (listed on on the vehicle) possibly in red colour
Should not have
• No plumbing symbols, pictures or icons

```html
<!DOCTYPE html>
<html lang="en">
<head>
<meta charset="utf-8">
<title>Brightwater Plumbing &amp; Gas Services – Vehicle Wrap</title>
<link href="https://fonts.googleapis.com/css2?family=Open+Sans:ital,wght@0,400;0,700;1,700&display=swap" rel="stylesheet">
<style>
  :root {
    --brand-yellow: #fbed22;
    --wrap-white: #ffffff;
    --ink: #111111;
    --alert-red: #d9141b;
    --glass: #3a3f45;
    --tyre: #1c1c1c;
    --rim: #c9cdd1;
    --canvas: #eef0f2;
    --panel-line: #d5d8db;
  }
  html, body {
    margin: 0;
    padding: 0;
    width: 1200px;
    height: 900px;
    overflow: hidden;
    background: var(--canvas);
  }
  .wrap-design {
    width: 1200px;
    height: 900px;
    display: block;
  }
  .body-white { fill: var(--wrap-white); stroke: var(--panel-line); stroke-width: 2; }
  .body-yellow { fill: var(--brand-yellow); }
  .window { fill: var(--glass); }
  .tyre { fill: var(--tyre); }
  .rim { fill: var(--rim); }
  .panel-seam { stroke: var(--panel-line); stroke-width: 2; fill: none; }
  .emergency-hours {
    font-family: "Open Sans", sans-serif;
    font-weight: 700;
    font-size: 46px;
    fill: var(--alert-red);
  }
  .emergency-label {
    font-family: "Open Sans", sans-serif;
    font-weight: 400;
    font-size: 23px;
    fill: var(--alert-red);
  }
  .motto {
    font-family: "Open Sans", sans-serif;
    font-weight: 700;
    font-style: italic;
    font-size: 36px;
    fill: var(--ink);
  }
  .company-name {
    font-family: "Open Sans", sans-serif;
    font-weight: 700;
    fill: var(--ink);
  }
</style>
</head>
<body>
<svg class="wrap-design" viewBox="0 0 1200 900" xmlns="http://www.w3.org/2000/svg">
  <!-- roof rack -->
  <g class="roof-rack">
    <rect class="body-yellow" x="310" y="196" width="650" height="12"/>
    <path class="body-yellow" d="M360 206 L600 268 L600 282 L352 216 Z"/>
  </g>

  <!-- cab -->
  <g class="cab">
    <path class="body-white" d="M20 340 Q30 320 250 300 L320 235 L600 235 L600 525 L20 525 Z"/>
    <path class="body-yellow" d="M20 340 Q30 320 250 300 L320 235 L600 235 L600 300 Q420 300 330 350 Q220 410 190 520 L20 520 Z"/>
    <path class="window" d="M262 305 L325 245 L470 245 L470 320 L262 320 Z"/>
    <path class="window" d="M490 245 L580 245 L580 315 L490 315 Z"/>
    <line class="panel-seam" x1="480" y1="240" x2="480" y2="515"/>
    <text class="company-name" x="430" y="425" text-anchor="middle" font-size="33">BRIGHTWATER</text>
    <text class="company-name" x="430" y="455" text-anchor="middle" font-size="18">PLUMBING &amp; GAS SERVICES</text>
  </g>

  <!-- service body -->
  <g class="service-body">
    <rect class="body-white" x="615" y="215" width="480" height="310"/>
    <path class="body-yellow" d="M615 215 L985 215 Q820 320 640 360 L615 365 Z"/>
    <line class="panel-seam" x1="975" y1="220" x2="975" y2="520"/>
    <rect role="img" aria-label="Cartoon plumber in overalls and cap holding a large pipe wrench and a plunger" x="865" y="232" width="200" height="280" rx="10" fill="#5b7fa8" opacity="0.55"/>
    <text class="emergency-hours" x="665" y="282">24hr</text>
    <text class="emergency-label" x="668" y="310">Emergency</text>
    <text class="emergency-label" x="680" y="334">service</text>
    <text class="motto" x="648" y="380">The Reliable</text>
    <text class="motto" x="648" y="420">Plumbing Specialists</text>
  </g>

  <!-- wheels -->
  <g class="wheels">
    <circle class="tyre" cx="125" cy="540" r="70"/>
    <circle class="rim" cx="125" cy="540" r="40"/>
    <circle class="tyre" cx="755" cy="540" r="70"/>
    <circle class="rim" cx="755" cy="540" r="40"/>
  </g>
</svg>
</body>
</html>
```